KT7 ‘Reveal Your KT7 Winning Path’

‘Reveal Your KT7 Winning Path ‘ this pay of ok , and also the logo, but i need a cover for one pdf A4, KT7 is a product for discovery the skill in human resource

See below link to serve as inspiration reference in creating your design proposals. Thank you.

kt7careerguild.com
Updates

ce systeme artmerchy pas tros claire,j ai acheter 70 dessins et ont me demande contuement des trucs a faire bah

Target Market(s)

https://kt7careerguild.com/available-reports/ i work for this company

Industry/Entity Type

Business Consultant

Font styles to use
Serif

Colors
3176b5
3276b5
6cbee2
85abd2
3277b5

Requirements
Must have
• Look the link and product Report KT7, i need professional and istutional look And on cover ‘Reveal your KT7 Winning Path’
Nice to have
• front blue and Grey , silver, look my files , i need the silver Logo Kt7 , Genotric stile
Should not have
• fantasy,

```html
<!DOCTYPE html>
<html lang="en">
<head>
<meta charset="utf-8">
<title>Reveal Your KT7 Winning Path — Report Cover</title>
<link rel="stylesheet" href="https://fonts.googleapis.com/css2?family=Libre+Caslon+Text:wght@700&display=swap">
<style>
  :root {
    --page-bg: #e9ecef;
    --blue-deep: #1a3fd6;
    --blue-mid: #3176b5;
    --blue-soft: #85abd2;
    --cyan-glow: #6cbee2;
    --teal-dark: #0f4a6e;
    --title-ink: #1b1b1d;
    --title-halo: #ffffff;
    --silver: #c9ccd2;
  }
  * { box-sizing: border-box; margin: 0; padding: 0; }
  html, body {
    width: 1200px;
    height: 800px;
    overflow: hidden;
    background: var(--page-bg);
  }
  .canvas {
    position: relative;
    width: 1200px;
    height: 800px;
  }
  .report-cover {
    position: absolute;
    left: 345px;
    top: 40px;
    width: 510px;
    height: 720px;
    overflow: hidden;
    background:
      radial-gradient(ellipse 55% 42% at 50% 50%, rgba(165,235,245,0.85) 0%, rgba(108,190,226,0.55) 38%, rgba(49,118,181,0) 78%),
      linear-gradient(180deg, var(--blue-deep) 0%, #1f5fb8 28%, var(--teal-dark) 55%, #1a55b8 80%, var(--blue-deep) 100%);
  }
  .science-artwork {
    position: absolute;
    inset: 0;
    width: 100%;
    height: 100%;
  }
  .cover-title {
    position: absolute;
    top: 112px;
    left: 0;
    width: 100%;
    text-align: center;
    font-family: "Libre Caslon Text", Georgia, serif;
    font-weight: 700;
    color: var(--title-ink);
    text-transform: uppercase;
    line-height: 1;
    text-shadow:
      0 0 3px var(--title-halo),
      0 0 6px var(--title-halo),
      0 0 10px rgba(255,255,255,0.7);
  }
  .cover-title span { display: block; }
  .title-reveal  { font-size: 66px; letter-spacing: 1px; }
  .title-brand   { font-size: 46px; margin-top: 12px; }
  .title-winning { font-size: 62px; margin-top: 12px; }
  .title-path    { font-size: 90px; margin-top: 10px; }
  .brand-mark {
    position: absolute;
    left: 50%;
    top: 590px;
    transform: translateX(-50%);
    display: flex;
    align-items: center;
    gap: 12px;
    font-family: "Libre Caslon Text", Georgia, serif;
    font-weight: 700;
    font-size: 30px;
    color: var(--silver);
  }
  .brand-mark .brand-dot {
    width: 64px;
    height: 64px;
    border: 5px solid var(--silver);
    border-radius: 50%;
  }
</style>
</head>
<body>
<main class="canvas">
  <section class="report-cover">
    <svg class="science-artwork" viewBox="0 0 510 720" role="img" aria-label="Background illustration of molecular structures and a glowing DNA double helix">
      <defs>
        <radialGradient id="helixGlow" cx="0.5" cy="0.5" r="0.5">
          <stop offset="0" stop-color="#3ab6d0" stop-opacity="0.5"/>
          <stop offset="0.6" stop-color="#2a7fc0" stop-opacity="0.22"/>
          <stop offset="1" stop-color="#1a3fd6" stop-opacity="0"/>
        </radialGradient>
        <radialGradient id="moleculeShade" cx="0.5" cy="0.5" r="0.5">
          <stop offset="0" stop-color="#0d2f6e" stop-opacity="0.45"/>
          <stop offset="1" stop-color="#0d2f6e" stop-opacity="0"/>
        </radialGradient>
      </defs>
      <ellipse cx="300" cy="590" rx="330" ry="120" fill="url(#helixGlow)" transform="rotate(-14 300 590)"/>
      <ellipse cx="430" cy="110" rx="120" ry="90" fill="url(#moleculeShade)"/>
      <ellipse cx="60" cy="360" rx="90" ry="110" fill="url(#moleculeShade)"/>
      <ellipse cx="440" cy="660" rx="110" ry="70" fill="url(#moleculeShade)"/>
    </svg>

    <h1 class="cover-title">
      <span class="title-reveal">Reveal</span>
      <span class="title-brand">Your KT7</span>
      <span class="title-winning">Winning</span>
      <span class="title-path">Path</span>
    </h1>

    <div class="brand-mark">
      <span class="brand-dot"></span>
      <span class="brand-name">KT7</span>
    </div>
  </section>
</main>
</body>
</html>
```